Business Card Design

Business sales of reconditioned / used batteries with mobile delivery and install services. Customers base majority are auto car sales lots and individuals.

Card need to convey quality product reliability and quick prompt professional service.

Card must reflect excellence in customer care and product being offered

Target Market(s)

Auto car lots new and used. Auto repair shops. Individuals.

Industry/Entity Type

Business

Contact Information for Business Card

Batteries Q-Volt
Cars, Trucks, Boats, Motorcycles, lawn mowers, power tools
Delivery & install available most vehicles
Mon-Sat 9-6pm
Dale Morrick 501-738-2056
*product warranty 6 month shelf life battery/1 year blems battery

```html
<!DOCTYPE html>
<html lang="en">
<head>
<meta charset="utf-8">
<title>Batteries Q-Volt – Business Card</title>
<link rel="stylesheet" href="https://fonts.googleapis.com/css2?family=Baloo+2:wght@700&family=Didact+Gothic&family=Delius&family=PT+Sans&display=swap">
<style>
  :root {
    --card-green: #0a774b;
    --paper: #ffffff;
    --blush: #f6cfe0;
    --lemon: #f2e600;
    --bark: #6b5030;
    --rule-light: #ffffff;
    --rule-tan: #b8b89a;
  }
  * { margin: 0; padding: 0; box-sizing: border-box; }
  html, body { width: 1200px; height: 683px; overflow: hidden; background: var(--paper); }
  .card { position: relative; width: 1200px; height: 683px; background: var(--paper); }
  .card-face {
    position: absolute; left: 24px; top: 14px; width: 1154px; height: 656px;
    background: var(--card-green);
  }
  .divider { position: absolute; left: 24px; width: 1154px; height: 4px; }
  .divider-top { top: 305px; }
  .divider-bottom { top: 505px; }
  .line { position: absolute; white-space: nowrap; }
  .owner-name {
    left: 0; width: 1178px; top: 148px; text-align: center;
    font-family: "Baloo 2", sans-serif; font-weight: 700; font-size: 50px;
    color: var(--blush); line-height: 1;
  }
  .owner-phone {
    left: 0; width: 1178px; top: 234px; text-align: center;
    font-family: "Didact Gothic", sans-serif; font-size: 33px;
    color: var(--paper); line-height: 1;
  }
  .company-name {
    left: 24px; width: 1190px; top: 356px; text-align: center;
    font-family: "Didact Gothic", sans-serif; font-size: 58px;
    color: var(--blush); line-height: 1; letter-spacing: 1px;
  }
  .company-hours {
    left: 24px; width: 1190px; top: 432px; text-align: center;
    font-family: "Delius", cursive; font-size: 33px;
    color: var(--lemon); line-height: 1;
  }
  .services {
    left: 100px; font-family: "Delius", cursive; font-size: 32px;
    color: var(--lemon); line-height: 1; letter-spacing: 1.2px;
  }
  .services-range { top: 518px; }
  .services-delivery { top: 562px; }
  .warranty-band {
    position: absolute; left: 31px; top: 619px; width: 1142px; height: 41px;
    background: var(--paper);
  }
  .warranty-text {
    left: 100px; top: 621px; font-family: "PT Sans", sans-serif; font-size: 31px;
    color: var(--bark); line-height: 1.15;
  }
</style>
</head>
<body>
<main class="card">
  <div class="card-face"></div>

  <p class="line owner-name">Dale Morrick</p>
  <p class="line owner-phone">Mobile : 501-738-2056</p>

  <svg class="divider divider-top" viewBox="0 0 1154 4" preserveAspectRatio="none" aria-hidden="true">
    <rect width="1154" height="4" fill="var(--rule-light)"/>
    <g fill="var(--rule-tan)">
      <rect x="0" width="6" height="4"/><rect x="178" width="6" height="4"/><rect x="196" width="30" height="4"/>
      <rect x="400" width="20" height="4"/><rect x="580" width="40" height="4"/><rect x="800" width="20" height="4"/>
      <rect x="985" width="20" height="4"/><rect x="1010" width="144" height="4"/>
    </g>
  </svg>

  <h1 class="line company-name">Batteries Q-Volt</h1>
  <p class="line company-hours">Mon-Sat : 9 am - 6pm</p>

  <svg class="divider divider-bottom" viewBox="0 0 1154 4" preserveAspectRatio="none" aria-hidden="true">
    <rect width="1154" height="4" fill="var(--rule-light)"/>
    <g fill="var(--rule-tan)">
      <rect x="0" width="180" height="4"/><rect x="190" width="12" height="4"/><rect x="370" width="40" height="4"/>
      <rect x="520" width="20" height="4"/><rect x="760" width="40" height="4"/><rect x="990" width="20" height="4"/>
      <rect x="1020" width="134" height="4"/>
    </g>
  </svg>

  <p class="line services services-range">Cars, Trucks, Boats, Motorcycles, lawn mowers, power tools</p>
  <p class="line services services-delivery">Delivery &amp; install available most vehicles Mon-Sat 9-6pm</p>

  <div class="warranty-band"></div>
  <p class="line warranty-text">Product Warranty&nbsp; : 6 month Shelf Life Battery/1 year Blems Battery</p>
</main>
</body>
</html>
```